7 3/4 x 5 1/4 Annual Banquet Invitation

Design an invitation for our Chamber's annual banquet. It will be a single sided invitation 5 1/4" wide by 7 3/4" height that we will print in-house. Our logo is attached. The theme is "Serving Together". I was thinking of an image with two hands coming together in a handshake, perhaps intertwining our logo colors. This is just a thought. I am open for any suggestions! Text for the invitation should be as follows: The Board of Directors and Staff cordially invites you to attend the 64th Yearly Gathering & Micro-Trade Fair - Monday, January 22, 2018. 5:30 p.m. Social, 6:00 p.m. Dinner. Cedarvale Chapel, 4819 Harlan P. Moss Rd S, Whiteville. Please RSVP by January 18, 2018.

Target Market(s)

This invitation will be printed and mailed to our membership.

Industry/Entity Type

Business Management

Colors
33a6d7
faa54b
0355a3
00a990

Requirements
Must have
• Event info as indentified above.
Nice to have
• Our Logo

```html
<!DOCTYPE html>
<html lang="en">
<head>
<meta charset="utf-8">
<title>Serving Together – Annual Banquet Invitation</title>
<link rel="stylesheet" href="https://fonts.googleapis.com/css2?family=Overpass:wght@600&family=Source+Sans+3:wght@400;600;700&family=Damion&display=swap">
<style>
  :root {
    --navy: #2a3990;
    --band: #283a93;
    --orange: #f7931e;
    --paper: #e6e7e8;
    --white: #ffffff;
    --photo-top: #3f3f8f;
    --photo-mid: #b99a96;
    --photo-warm: #f2b77a;
    --photo-low: #e9e2de;
  }
  * { margin: 0; padding: 0; box-sizing: border-box; }
  html, body {
    width: 943px; height: 1200px; overflow: hidden;
    background: var(--white);
  }
  .invitation {
    position: relative; width: 943px; height: 1200px; overflow: hidden;
    font-family: "Source Sans 3", "Myriad Pro", sans-serif;
    color: var(--navy);
  }
  .backdrop { position: absolute; inset: 0; }
  .headline {
    position: absolute; top: 58px; left: 0; right: 0;
    text-align: center;
    font-family: "Overpass", sans-serif; font-weight: 600;
    font-size: 62px; letter-spacing: 2px;
    color: var(--white);
  }
  .invite-copy {
    position: absolute; left: 0; right: 0;
    text-align: center; white-space: nowrap;
  }
  .invite-copy.lead, .invite-copy.event {
    font-size: 31px; font-weight: 400; text-transform: uppercase;
    line-height: 1;
  }
  .invite-copy.lead { top: 580px; }
  .invite-copy.script {
    top: 618px;
    font-family: "Damion", cursive;
    font-size: 56px; color: var(--orange); line-height: 1;
  }
  .invite-copy.event { top: 686px; }
  .date-band {
    position: absolute; top: 752px; left: 0; right: 0; height: 85px;
    background: var(--band); color: var(--white);
    display: flex; flex-direction: column; justify-content: center; align-items: center;
    font-weight: 700; font-size: 27px; line-height: 1.35;
  }
  .venue {
    position: absolute; top: 880px; left: 0; right: 0;
    display: flex; justify-content: center; align-items: center; gap: 8px;
    font-size: 21px; font-weight: 400;
  }
  .venue svg { width: 16px; height: 22px; flex: none; }
  .rsvp {
    position: absolute; top: 926px; left: 0; right: 0; text-align: center;
    font-size: 28px; color: var(--orange);
  }
  .website {
    position: absolute; left: 58px; top: 1154px;
    font-size: 25px; font-weight: 400;
  }
  .chamber {
    position: absolute; right: 20px; top: 1050px; width: 330px;
    display: flex; flex-direction: column; align-items: center; gap: 10px;
  }
  .chamber .mark {
    width: 58px; height: 58px; border-radius: 50%;
    background: var(--navy);
  }
  .chamber .name {
    font-weight: 700; font-size: 22px; line-height: 1.05;
    color: var(--navy); text-align: center; text-transform: uppercase;
  }
</style>
</head>
<body>
<main class="invitation">
  <svg class="backdrop" width="943" height="1200" viewBox="0 0 943 1200">
    <defs>
      <linearGradient id="photoTone" x1="0" y1="0" x2="0" y2="1">
        <stop offset="0" stop-color="var(--photo-top)"/>
        <stop offset="0.35" stop-color="var(--photo-mid)"/>
        <stop offset="0.6" stop-color="var(--photo-warm)"/>
        <stop offset="1" stop-color="var(--photo-low)"/>
      </linearGradient>
    </defs>
    <rect class="paper" width="943" height="1200" fill="var(--paper)"/>
    <path class="hero-photo" role="img" aria-label="Photo of two business people shaking hands in front of a softly lit, blurred city building"
          d="M0 0 H943 V512 C600 515 250 470 0 338 Z" fill="url(#photoTone)"/>
    <path class="top-white" d="M0 338 C250 470 600 515 943 512 V545 C600 550 250 530 0 400 Z" fill="var(--white)"/>
    <path class="top-swoosh" d="M0 338 C250 470 600 515 943 512 V526 C600 534 250 510 0 382 Z" fill="var(--orange)"/>
    <path class="bottom-white" d="M0 1104 C400 1080 760 1000 943 860 V1200 H0 Z" fill="var(--white)"/>
    <path class="bottom-swoosh" d="M0 1112 C400 1088 760 1010 943 876 V902 C760 1040 400 1112 0 1126 Z" fill="var(--orange)"/>
  </svg>

  <h1 class="headline">SERVING TOGETHER</h1>

  <p class="invite-copy lead">The Board of Directors and Staff Cordially</p>
  <p class="invite-copy script">invites you to attend</p>
  <p class="invite-copy event">The 64th Yearly Gathering &amp; Micro-Trade Fair</p>

  <div class="date-band">
    <span>Monday, January 22, 2018. 5:30 p.m.</span>
    <span>Social, 6:00 p.m. Dinner.</span>
  </div>

  <p class="venue">
    <svg viewBox="0 0 16 22" aria-hidden="true"><path d="M8 0C3.6 0 0 3.5 0 7.9 0 13.5 8 22 8 22s8-8.5 8-14.1C16 3.5 12.4 0 8 0zm0 11a3 3 0 1 1 0-6 3 3 0 0 1 0 6z" fill="var(--navy)"/></svg>
    <span>Cedarvale Chapel, 4819 Harlan P. Moss Rd S, Whiteville.</span>
  </p>
  <p class="rsvp">Please RSVP by January 18, 2018.</p>

  <p class="website">harborlinechamber.com</p>

  <div class="chamber">
    <span class="mark" aria-hidden="true"></span>
    <p class="name">Harborline Chamber<br>of Commerce &amp; Tourism</p>
  </div>
</main>
</body>
</html>
```